Flex Forward Thaw 21 day Challenge

We are having a Flex Forward Thaw Challenge at our fitness studio. We need a poster design using the template attached as a reference. I have also included our Molvaro logo to put on the poster. Please DO NOT use the graphics in the flyer as we are expecting something much better :-)

-Size needed 11x17 with bleeding for printing

-We need this made in Photoshop (CS3 friendly) or at least delivered in PS as we might change some text or re-arrange the design later on.

-We need this in layers.

```html
<!DOCTYPE html>
<html lang="en">
<head>
<meta charset="utf-8">
<title>Flex Forward Thaw 21 day Challenge – Molvaro</title>
<link rel="stylesheet" href="https://fonts.googleapis.com/css2?family=Fredoka:wght@600;700&family=Arimo:wght@700&display=swap">
<style>
  :root {
    --page: #ffffff;
    --navy: #0b1670;
    --ocean: #1c63d0;
    --ocean-light: #3d8ee6;
    --foam: #eef6fb;
    --sand: #e7d3a6;
    --sand-deep: #d9bf8a;
    --cream: #fff3a8;
    --cream-glow: #fffbe0;
    --rust: #b3533a;
    --gold: #f6e07a;
    --white: #ffffff;
    --cta-blue: #1a55c9;
    --cta-navy: #0c2a86;
    --ink: #1a1a1a;
  }
  * { margin: 0; padding: 0; box-sizing: border-box; }
  html, body { width: 796px; height: 1200px; overflow: hidden; background: var(--page); }
  body { position: relative; font-family: "Arimo", Arial, sans-serif; }

  .poster {
    position: absolute; left: 35px; top: 38px; width: 726px; height: 1124px;
    background: linear-gradient(to bottom, var(--navy) 0%, var(--navy) 52%, #1640a8 66%, var(--ocean) 76%, var(--ocean-light) 84%);
    overflow: hidden;
  }

  .beach-scene {
    position: absolute; left: 0; bottom: 0; width: 100%; height: 260px;
    background: linear-gradient(to bottom,
      rgba(255,255,255,0) 0%, rgba(238,246,251,0.85) 16%, var(--foam) 26%,
      #efe6cc 38%, var(--sand) 52%, var(--sand-deep) 100%);
  }

  .brand {
    position: absolute; left: 220px; top: 56px; width: 286px; height: 94px;
    background: var(--white); border: 3px solid var(--ink); border-radius: 6px;
    display: flex; align-items: center; justify-content: center; gap: 12px;
  }
  .brand-mark { width: 22px; height: 22px; background: var(--ink); }
  .brand-name { font-family: "Arimo", Arial, sans-serif; font-weight: 700; font-size: 38px; color: var(--ink); letter-spacing: 2px; }

  .title { position: absolute; left: 0; width: 100%; text-align: center; line-height: 1; }
  .title-word {
    display: block; font-family: "Fredoka", "Baloo 2", sans-serif; font-weight: 700;
    color: var(--cream); -webkit-text-stroke: 4px var(--rust); paint-order: stroke fill;
    text-shadow: 0 0 18px rgba(255,251,224,0.75), 0 0 36px rgba(255,240,170,0.45);
  }
  .title-big { font-size: 150px; }
  .title-small { font-size: 64px; -webkit-text-stroke: 3px var(--rust); }
  .title-line-1 { top: 178px; }
  .title-line-2 { top: 325px; }
  .title-line-3 { top: 382px; }

  .headline {
    position: absolute; left: 0; top: 532px; width: 100%; text-align: center;
    color: var(--gold); font-size: 27px; line-height: 33px; font-weight: 700; text-transform: uppercase;
  }

  .benefits {
    position: absolute; left: 140px; top: 596px; width: 540px; list-style: none;
    color: var(--white); font-size: 14px; line-height: 17px; font-weight: 700;
  }
  .benefits li { position: relative; padding-left: 15px; margin-bottom: 0; }
  .benefits li::before {
    content: ""; position: absolute; left: 0; top: 5px; width: 7px; height: 7px; border-radius: 50%; background: var(--white);
  }

  .offer { position: absolute; left: 0; width: 100%; text-align: center; color: var(--gold); font-weight: 700; text-transform: uppercase; }
  .offer-value { top: 690px; font-size: 28px; }
  .offer-price { top: 722px; font-size: 33px; display: flex; align-items: center; justify-content: center; gap: 10px; }
  .offer-price .rule { width: 98px; height: 3px; background: var(--gold); }

  .testimonial { position: absolute; left: 0; top: 775px; width: 100%; text-align: center; color: var(--white); font-weight: 700; }
  .testimonial-quote { font-size: 19px; }
  .testimonial-author { font-size: 12px; margin-top: 8px; }

  .cta { position: absolute; left: 0; top: 1008px; width: 100%; text-align: center; font-weight: 700; text-transform: uppercase; line-height: 21px; }
  .cta-urgency { color: var(--cta-blue); font-size: 18px; }
  .cta-action { color: var(--cta-navy); font-size: 18px; }
</style>
</head>
<body>
  <main class="poster">
    <div class="beach-scene" role="img" aria-label="Illustrated beach with ocean waves washing onto sand, footprints and a heart drawn in the sand"></div>

    <div class="brand">
      <span class="brand-mark"></span>
      <span class="brand-name">MOLVARO</span>
    </div>

    <h1>
      <span class="title title-line-1"><span class="title-word title-big">flex</span></span>
      <span class="title title-line-2"><span class="title-word title-small">forward</span></span>
      <span class="title title-line-3"><span class="title-word title-big">thaw</span></span>
    </h1>

    <p class="headline">Discover the secret to a<br>beach-ready body in just 21 days!</p>

    <ul class="benefits">
      <li>9 total training sessions designed to incinerate fat off your midsection, thighs, and arms</li>
      <li>21 days of nutritional guidance, including delicious recipes</li>
      <li>A Success Session to map out your individual plan for success</li>
      <li>Your very own Personal Accountability Coach to ensure you get results</li>
    </ul>

    <p class="offer offer-value">You get all this—a $399 value</p>
    <p class="offer offer-price"><span class="rule"></span>For only $99!<span class="rule"></span></p>

    <blockquote class="testimonial">
      <p class="testimonial-quote">I've never been more fit in my life—at age 41!</p>
      <p class="testimonial-author">~Marisol Kettering</p>
    </blockquote>

    <div class="cta">
      <p class="cta-urgency">Hurry! Space is limited to only 20 participants!!!</p>
      <p class="cta-action">Claim your spot now</p>
    </div>
  </main>
</body>
</html>
```